BQ7VOLN PSD Web Designs

We need website page designs for Toren Capital, a start up HEDGE FUND MANAGEMENT business. 

Toren means 'wave' in Greek, but this is not a Greek company.

You will need to create one template that will have some common elements (such as the menu) which you will then need to apply to 6 different pages.  

The site should:
• Incorporate the Toren logo, colours and graphic elements provided with this brief.
• Have a corporate look with the provided corporate colours used in design. 
• Be professional and user-friendly 
• Have an international feel
• Be clean, clear and and easy to read
• Information to be organised in an easily accessible and logical way for time-pressed business people who are looking for efficient ways to check and manage their investment portfolios online.

We are looking for:
• Designs that do not just copy the wireframe
• Original thinking
• Extension of the brand that has already been created, throughout site.
• Design x-factor (structure, layout, readability, graphic elements)
• Corporate feel
• Judicious use of imagery (only use stock photos if they ADD meaning to your designs).

WIREFRAMES:
Attached are the wireframes of the pages that need to be designed.

Target Market(s)

Adults based in US, UK and Asia Pacific aged 25 to 70 who are corporate investors

Requirements
Must have
• Your submissions must:
• Include the logo we have attached and tie in with the business card look
• Use the menu as per the wireframes
• Include 6 PSDs (one for each of the attached wireframes)
1. Home
2. Contact Us
3. DIsclaimer
4. Our Focus
5. Privacy Policy
6. Risk Profile

```html
<!DOCTYPE html>
<html lang="en">
<head>
<meta charset="utf-8">
<title>Toren Capital – Web Page Designs</title>
<link href="https://fonts.googleapis.com/css2?family=Cinzel:wght@600;700&family=Arimo:wght@400;700&display=swap" rel="stylesheet">
<style>
:root{
  --navy:#15305e;
  --blue:#1670bf;
  --blue-dark:#0f5ea8;
  --sky:#34a6e3;
  --pale:#c6e6f7;
  --teal:#1f9c98;
  --strip:#d9dde2;
  --band:#d4d6d9;
  --text:#6b6f75;
  --frame-top:#545557;
  --frame-bottom:#a2a3a6;
}
*{box-sizing:border-box;margin:0;padding:0}
html,body{width:1200px;height:4862px;overflow:hidden;background:#fff}
body{position:relative;font-family:"Arimo",Arial,sans-serif;color:var(--text)}
.board{position:absolute;left:180px;width:860px;background:linear-gradient(var(--frame-top) 0%,#5c5d5f 45%,var(--frame-bottom) 100%)}
.page{position:absolute;left:82px;width:686px;background:#fff;border-bottom-right-radius:30px;overflow:hidden}
.credit{position:absolute;right:86px;font-size:6px;color:#eef1f5}
/* header */
.site-header{position:relative;height:44px;background:#fff}
.site-header svg{position:absolute;left:0;top:0}
.brand{position:absolute;left:18px;top:14px;display:flex;align-items:center;gap:6px;font-family:"Cinzel",serif;font-weight:700;font-size:15px;color:var(--navy);letter-spacing:.3px}
.brand-mark{width:9px;height:9px;background:var(--blue)}
.nav{position:absolute;left:214px;top:0;height:44px;display:flex}
.nav a{font-family:"Cinzel",serif;font-weight:700;font-size:8.5px;color:#fff;text-decoration:none;padding:0 14px;line-height:44px;border-right:1px solid rgba(255,255,255,.35);letter-spacing:.4px}
.nav a.current{color:#5aa9e0}
.entity{position:absolute;right:14px;top:0;line-height:44px;font-family:"Cinzel",serif;font-size:7px;color:#a9d2f0;letter-spacing:.3px}
.strip{height:7px;background:var(--strip)}
/* content */
.content{position:relative;padding:14px 0 0 16px}
.main{width:515px}
h1{font-family:"Cinzel",serif;font-weight:700;font-size:15px;color:var(--navy);letter-spacing:.6px;margin-bottom:6px}
h2{font-family:"Cinzel",serif;font-weight:600;font-size:9px;color:var(--blue);letter-spacing:.3px;margin:6px 0 2px}
h3{font-size:6px;font-weight:700;color:var(--teal);margin:7px 0 2px}
p{font-size:5.5px;line-height:7.6px;color:var(--text);margin-bottom:6px}
.lead{font-size:6px;color:var(--teal);margin-bottom:2px}
.sidebar{position:absolute;right:0;top:20px;width:120px}
.sidebar a{display:block;font-size:7.5px;color:var(--blue);text-decoration:none;padding:3px 0 2px;border-bottom:1px solid var(--pale)}
.sidebar .gap{height:8px}
/* footer */
.site-footer{position:absolute;left:0;bottom:0;width:686px;height:28px;background:var(--band)}
.footer-accent{position:absolute;right:0;top:0;width:170px;height:28px;background:var(--blue)}
.footer-accent::before{content:"";position:absolute;left:-40px;top:0;width:40px;height:28px;background:var(--sky)}
.footer-links{position:absolute;left:16px;top:10px;display:flex;gap:10px}
.footer-links a{font-family:"Cinzel",serif;font-size:6.5px;color:#7e8288;text-decoration:none;padding-right:10px;border-right:1px solid #b5b8bc}
.footer-links a:last-child{border:0}
.footer-links a.current{color:var(--sky)}
/* imagery */
.photo{display:block}
.hero{position:relative;height:150px;background:linear-gradient(#d7e4ee 0%,#c3d5e2 45%,#7b8f5b 72%,#3e5b23 100%)}
.quote{position:absolute;left:16px;top:22px;width:240px;font-size:15.5px;line-height:17px;color:#2791d8}
.quote b{font-family:"Cinzel",serif;font-size:20px;color:var(--blue)}
.photo-row{display:flex;gap:2px;width:515px;height:118px;margin:4px 0 10px}
.photo-row div{flex:1}
/* contact */
.contact-lines{font-size:5.5px;line-height:7.5px;margin-bottom:10px}
.dashed{border-top:1px dashed #b8bcc0;width:500px;margin:4px 0 8px}
.label{font-size:5.5px;color:#555;margin-bottom:3px}
.label small{font-size:4px;color:#888}
.field{width:308px;height:11px;border:1px solid #3f8cd0;margin-bottom:10px}
.phone-row{display:flex;align-items:center;gap:6px;font-size:5px;color:#777;margin-bottom:10px}
.phone-row span.box{display:inline-block;height:11px;border:1px solid #3f8cd0}
.radio-row{display:flex;gap:38px;font-size:5px;color:#777;margin-bottom:12px}
.radio-row span::before{content:"";display:inline-block;width:10px;height:10px;border:1px solid #3f8cd0;border-radius:50%;vertical-align:middle;margin-right:4px}
.section-label{font-size:7px;color:#7a7e84;margin-bottom:6px}
.textarea{width:308px;height:84px;border:1px solid #3f8cd0;margin-bottom:14px}
.submit{display:inline-block;background:var(--blue);color:#fff;font-size:6px;font-weight:700;padding:3px 6px;letter-spacing:.3px}
/* risk */
.chart-title{font-family:"Cinzel",serif;font-weight:600;font-size:8.5px;color:var(--navy);letter-spacing:.3px}
.risk-grid{position:relative;height:470px}
.risk-grid > *{position:absolute}
.vrule{width:1px;background:#d3d6da}
table{border-collapse:collapse;width:152px;font-size:4px;color:#555}
caption{background:var(--blue-dark);color:#fff;text-align:left;font-size:4.5px;padding:2px 3px;caption-side:top}
th{background:#2a8ac9;color:#fff;font-weight:400;padding:1.5px 3px;text-align:left}
td{padding:1.5px 3px;border-bottom:1px solid #fff}
tr:nth-child(odd) td{background:#dff0f0}
tr:nth-child(even) td{background:#eef7f7}
td:last-child,th:last-child{text-align:right}
</style>
</head>
<body>

<!-- ========== HOME ========== -->
<section class="board" style="top:128px;height:532px">
  <div class="page" style="top:52px;height:428px">
    <header class="site-header">
      <svg width="686" height="44" viewBox="0 0 686 44"><path d="M200 0H686V44H180Z" fill="var(--blue)"/></svg>
      <div class="brand"><span class="brand-mark"></span>Toren Capital</div>
      <nav class="nav"><a>Our Focus</a><a>Contact Us</a></nav>
      <div class="entity">Toren Capital Pty. Ltd</div>
    </header>
    <div class="strip"></div>
    <div class="hero photo" role="img" aria-label="Businessman in a white shirt leaning back at a desk in an open green field under a pale sky">
      <div class="quote"><b>“</b> Lorem ipsum dolor sit congue amet, consectetur adi piscing elit. <b>”</b></div>
    </div>
    <div class="content">
      <div class="main" style="width:540px">
        <h1>Welcome</h1>
        <p>Lorem ipsum dolor sit amet, consectetur adipiscing elit. Nam pulvinar ultrices magna, nec blandit quam luctus id. Vivamus sagittis iaculis convallis. Phasellus vestibulum, ipsum nec vestibulum venenatis, erat lorem consequat tellus, tincidunt consequat neque ipsum id metus. Morbi at lorem purus, eu tristique turpis. Sed porta erat sed. Sed ac nibh ante. Mauris dolor nisi, auctor ut commodo non, aliquam et felis. Aliquam ornare aliquam adipiscing auctor. Fusce congue dictum ligula, non faucibus mi congue ut. Fusce facilisis pretium aliquet. Aenean ornare semper aliquet. Integer dolor felis, mollis at ullamcorper sit amet, mollis at velit.</p>
        <p>In sodales libero in turpis consectetur malesuada. Fusce ipsum orci, fringilla varius euismod pulvinar, accumsan sit amet est. Phasellus tincidunt adipiscing libero sed facilisis. Praesent facilisis, turpis eu cursus feugiat, nulla urna suscipit ligula, quis interdum elit ipsum ut ante. Donec euismod scelerisque egestas. Vivamus non mauris nec mauris scelerisque bibendum eget nec mauris. Aenean auctor, massa a interdum euismod, libero mi placerat leo, nec volutpat massa quam quis turpis.</p>
      </div>
    </div>
    <footer class="site-footer"><div class="footer-accent"></div><div class="footer-links"><a>Privacy Policy</a><a>Disclaimer</a></div></footer>
  </div>
  <div class="credit" style="top:488px">Toren Capital Pty Ltd</div>
</section>

<!-- ========== CONTACT US ========== -->
<section class="board" style="top:728px;height:860px">
  <div class="page" style="top:52px;height:752px">
    <header class="site-header">
      <svg width="686" height="44" viewBox="0 0 686 44"><path d="M200 0H686V44H180Z" fill="var(--blue)"/></svg>
      <div class="brand"><span class="brand-mark"></span>Toren Capital</div>
      <nav class="nav"><a>Our Focus</a><a class="current">Contact Us</a></nav>
      <div class="entity">Toren Capital Pty. Ltd</div>
    </header>
    <div class="strip"></div>
    <div class="content">
      <div class="main">
        <h1>Contact Us</h1>
        <h2>By Phone / Mail</h2>
        <div class="contact-lines">Toren Capital Pty Ltd<br>Level 12, 80 Harbour Lane<br>Southbank VIC 3006<br>Australia<br>T: +61 3 9000 1234<br>F: +61 3 9000 5678<br>E: info@torencapital.com.au</div>
        <div class="dashed" style="border:0;border-top:1px solid #d3d6da"></div>
        <h2 style="margin-top:-2px">Or Email</h2>
        <div class="section-label">YOUR DETAILS</div>
        <div class="dashed" style="margin-top:-6px"></div>
        <div class="label">First Name</div><div class="field"></div>
        <div class="label">Last Name</div><div class="field"></div>
        <div class="label">Contact Phone <small>(Please enter the preferred number you would like us to contact you on)</small></div>
        <div class="phone-row">Country Code <span class="box" style="width:26px"></span> Area Code <span class="box" style="width:26px"></span> Phone No <span class="box" style="width:80px"></span></div>
        <div class="label">Email Address <small>(Please enter the preferred email you would like us to contact you on)</small></div><div class="field"></div>
        <div class="label">Preferred Contact Method</div>
        <div class="radio-row"><span>Email</span><span style="margin-left:60px">Phone</span></div>
        <div class="section-label">YOUR ENQUIRY</div>
        <div class="dashed" style="margin-top:-6px"></div>
        <div class="label">Select Enquiry Category</div>
        <div class="radio-row"><span>Investor Enquiries</span><span>Career Enquiries</span><span>Other Enquiries</span></div>
        <div class="label">Further Description (Tell us more)</div>
        <div class="textarea"></div>
        <div class="submit">SUBMIT</div>
      </div>
      <aside class="sidebar"><a>Our Focus</a><a>Contact Us</a><div class="gap"></div><a>Quick Links</a><a>Toren Home</a><a>Contact Us</a></aside>
    </div>
    <footer class="site-footer"><div class="footer-accent"></div><div class="footer-links"><a>Privacy Policy</a><a>Disclaimer</a></div></footer>
  </div>
  <div class="credit" style="top:812px">Toren Capital Pty Ltd</div>
</section>

<!-- ========== DISCLAIMER ========== -->
<section class="board" style="top:1672px;height:721px">
  <div class="page" style="top:52px;height:616px">
    <header class="site-header">
      <svg width="686" height="44" viewBox="0 0 686 44"><path d="M200 0H686V44H180Z" fill="var(--blue)"/></svg>
      <div class="brand"><span class="brand-mark"></span>Toren Capital</div>
      <nav class="nav"><a>Our Focus</a><a>Contact Us</a></nav>
      <div class="entity">Toren Capital Pty. Ltd</div>
    </header>
    <div class="strip"></div>
    <div class="content">
      <div class="main">
        <h1>Disclaimer</h1>
        <h2 style="margin-top:-2px">Website Disclaimer - Terms and Conditions of Use</h2>
        <h3 style="margin-top:0">Intellectual Property Rights</h3>
        <p>Lorem ipsum dolor sit amet, consectetur adipiscing elit. Nam pulvinar ultrices magna, nec blandit quam luctus id. Vivamus sagittis iaculis convallis. Phasellus vestibulum, ipsum nec vestibulum venenatis, erat lorem consequat tellus, tincidunt consequat neque ipsum id metus. Morbi at lorem purus, eu tristique turpis. Sed porta erat sed. Sed ac nibh ante.</p>
        <p>Aliquam ornare aliquam adipiscing auctor. Fusce congue dictum ligula, non faucibus mi congue ut. Fusce facilisis pretium aliquet. Aenean ornare semper aliquet. Integer dolor felis, mollis at ullamcorper sit amet, mollis at velit. Vestibulum ante ipsum primis in faucibus orci luctus et ultrices posuere cubilia Curae.</p>
        <h3>Linking and Third Party Material</h3>
        <p>In sodales libero in turpis consectetur malesuada. Fusce ipsum orci, fringilla varius euismod pulvinar, accumsan sit amet est. Phasellus tincidunt adipiscing libero sed facilisis. Praesent facilisis, turpis eu cursus feugiat, nulla urna suscipit ligula, quis interdum elit ipsum ut ante. Donec euismod scelerisque egestas. Vivamus non mauris nec mauris scelerisque bibendum eget nec mauris. Donec interdum quam vitae orci suscipit varius. Aenean auctor, massa a interdum euismod, libero mi placerat leo, nec volutpat massa quam quis turpis. Morbi tortor magna, egestas vitae posuere at, congue eget magna. Nulla nec tellus sed metus facilisis sodales.</p>
        <h3>Release</h3>
        <p>In sodales libero in turpis consectetur malesuada. Fusce ipsum orci, fringilla varius euismod pulvinar, accumsan sit amet est. Aenean auctor, massa a interdum euismod, libero mi placerat leo, nec volutpat massa quam quis turpis. Morbi tortor magna, egestas vitae posuere at, congue eget magna. Nulla nec tellus sed metus facilisis sodales.</p>
        <h3>Jurisdiction</h3>
        <p>Aliquam ornare aliquam adipiscing auctor. Fusce congue dictum ligula, non faucibus mi congue ut. Fusce facilisis pretium aliquet. Aenean ornare semper aliquet. Integer dolor felis, mollis at ullamcorper sit amet, mollis at velit.</p>
        <h3>Further Information</h3>
        <p>Aenean auctor, massa a interdum euismod, libero mi placerat leo, nec volutpat massa quam quis turpis. Morbi tortor magna, egestas vitae posuere at, congue eget magna. Nam a orci at turpis accumsan ultrices et nec dui. Nulla nec tellus sed metus facilisis sodales.</p>
      </div>
      <aside class="sidebar"><a>Our Focus</a><a>Contact Us</a><div class="gap"></div><a>Quick Links</a><a>Toren Home</a><a>Contact Us</a></aside>
    </div>
    <footer class="site-footer"><div class="footer-accent"></div><div class="footer-links"><a>Privacy Policy</a><a class="current">Disclaimer</a></div></footer>
  </div>
  <div class="credit" style="top:676px">Toren Capital Pty Ltd</div>
</section>

<!-- ========== PRIVACY POLICY ========== -->
<section class="board" style="top:2462px;height:721px">
  <div class="page" style="top:52px;height:616px">
    <header class="site-header">
      <svg width="686" height="44" viewBox="0 0 686 44"><path d="M200 0H686V44H180Z" fill="var(--blue)"/></svg>
      <div class="brand"><span class="brand-mark"></span>Toren Capital</div>
      <nav class="nav"><a>Our Focus</a><a>Contact Us</a></nav>
      <div class="entity">Toren Capital Pty. Ltd</div>
    </header>
    <div class="strip"></div>
    <div class="content">
      <div class="main">
        <h1>Privacy Policy</h1>
        <div class="lead">Toren Capital PTY LTD (“TOREN”) is committed to good information privacy practices and maintaining your privacy when you visit our website</div>
        <h3 style="margin-top:0">Intellectual Property Rights</h3>
        <p>Lorem ipsum dolor sit amet, consectetur adipiscing elit. Nam pulvinar ultrices magna, nec blandit quam luctus id. Vivamus sagittis iaculis convallis. Phasellus vestibulum, ipsum nec vestibulum venenatis, erat lorem consequat tellus, tincidunt consequat neque ipsum id metus. Morbi at lorem purus, eu tristique turpis.</p>
        <p>Aliquam ornare aliquam adipiscing auctor. Fusce congue dictum ligula, non faucibus mi congue ut. Fusce facilisis pretium aliquet. Aenean ornare semper aliquet. Integer dolor felis, mollis at ullamcorper sit amet, mollis at velit. Vestibulum ante ipsum primis in faucibus orci luctus et ultrices posuere cubilia Curae.</p>
        <h3>Linking and Third Party Material</h3>
        <p>In sodales libero in turpis consectetur malesuada. Fusce ipsum orci, fringilla varius euismod pulvinar, accumsan sit amet est. Phasellus tincidunt adipiscing libero sed facilisis. Praesent facilisis, turpis eu cursus feugiat, nulla urna suscipit ligula, quis interdum elit ipsum ut ante. Donec euismod scelerisque egestas. Vivamus non mauris nec mauris scelerisque bibendum eget nec mauris. Aenean auctor, massa a interdum euismod, libero mi placerat leo, nec volutpat massa quam quis turpis. Morbi tortor magna, egestas vitae posuere at, congue eget magna. Nulla nec tellus sed metus facilisis sodales.</p>
        <h3>Release</h3>
        <p>In sodales libero in turpis consectetur malesuada. Aenean auctor, massa a interdum euismod, libero mi placerat leo, nec volutpat massa quam quis turpis. Morbi tortor magna, egestas vitae posuere at, congue eget magna. Nam a orci at turpis accumsan ultrices et nec dui. Nulla nec tellus sed metus facilisis sodales.</p>
        <h3>Jurisdiction</h3>
        <p>Aliquam ornare aliquam adipiscing auctor. Fusce congue dictum ligula, non faucibus mi congue ut. Fusce facilisis pretium aliquet. Aenean ornare semper aliquet. Integer dolor felis, mollis at ullamcorper sit amet.</p>
        <h3>Further Information</h3>
        <p>Aenean auctor, massa a interdum euismod, libero mi placerat leo, nec volutpat massa quam quis turpis. Morbi tortor magna, egestas vitae posuere at, congue eget magna. Nulla nec tellus sed metus facilisis sodales.</p>
      </div>
      <aside class="sidebar"><a>Our Focus</a><a>Contact Us</a><div class="gap"></div><a>Quick Links</a><a>Toren Home</a><a>Contact Us</a></aside>
    </div>
    <footer class="site-footer"><div class="footer-accent"></div><div class="footer-links"><a class="current">Privacy Policy</a><a>Disclaimer</a></div></footer>
  </div>
  <div class="credit" style="top:676px">Toren Capital Pty Ltd</div>
</section>

<!-- ========== OUR FOCUS ========== -->
<section class="board" style="top:3252px;height:656px">
  <div class="page" style="top:52px;height:552px">
    <header class="site-header">
      <svg width="686" height="44" viewBox="0 0 686 44"><path d="M200 0H686V44H180Z" fill="var(--blue)"/></svg>
      <div class="brand"><span class="brand-mark"></span>Toren Capital</div>
      <nav class="nav"><a class="current">Our Focus</a><a>Contact Us</a></nav>
      <div class="entity">Toren Capital Pty. Ltd</div>
    </header>
    <div class="strip"></div>
    <div class="content">
      <div class="main">
        <h1>Our Focus</h1>
        <div class="photo-row">
          <div class="photo" role="img" aria-label="Team of business professionals in dark suits" style="background:linear-gradient(#e8eaee,#8a8f98 55%,#2a2d33)"></div>
          <div class="photo" role="img" aria-label="Colleagues joining hands together in teamwork" style="background:linear-gradient(135deg,#f1f1f1,#b9b1a6 50%,#4a4d55)"></div>
          <div class="photo" role="img" aria-label="Magnifying glass over financial charts and figures" style="background:linear-gradient(135deg,#eef2f8,#9bb2d4 55%,#3a5a8e)"></div>
        </div>
        <p>Lorem ipsum dolor sit amet, consectetur adipiscing elit. Nam pulvinar ultrices magna, nec blandit quam luctus id. Vivamus sagittis iaculis convallis. Phasellus vestibulum, ipsum nec vestibulum venenatis, erat lorem consequat tellus, tincidunt consequat neque ipsum id metus. Morbi at lorem purus, eu tristique turpis. Sed porta erat sed. Sed ac nibh ante.</p>
        <p>Aliquam ornare aliquam adipiscing auctor. Fusce congue dictum ligula, non faucibus mi congue ut. Fusce facilisis pretium aliquet. Aenean ornare semper aliquet. Integer dolor felis, mollis at ullamcorper sit amet, mollis at velit. Vestibulum ante ipsum primis in faucibus orci luctus et ultrices posuere cubilia Curae. In sodales libero in turpis consectetur malesuada. Fusce ipsum orci, fringilla varius euismod pulvinar, accumsan sit amet est. Phasellus tincidunt adipiscing libero sed facilisis. Donec euismod scelerisque egestas. Vivamus non mauris nec mauris scelerisque bibendum eget nec mauris. Donec interdum quam vitae orci suscipit varius. Aenean auctor, massa a interdum euismod.</p>
      </div>
      <aside class="sidebar"><a>Our Focus</a><a>Contact Us</a><div class="gap"></div><a>Quick Links</a><a>Toren Home</a><a>Contact Us</a></aside>
    </div>
    <footer class="site-footer"><div class="footer-accent"></div><div class="footer-links"><a>Privacy Policy</a><a>Disclaimer</a></div></footer>
  </div>
  <div class="credit" style="top:612px">Toren Capital Pty Ltd</div>
</section>

<!-- ========== RISK MANAGEMENT ========== -->
<section class="board" style="top:3975px;height:875px">
  <div class="page" style="top:52px;height:768px">
    <header class="site-header">
      <svg width="686" height="44" viewBox="0 0 686 44"><path d="M200 0H686V44H180Z" fill="var(--blue)"/></svg>
      <div class="brand"><span class="brand-mark"></span>Toren Capital</div>
      <nav class="nav"><a>Our Focus</a><a>Contact Us</a></nav>
      <div class="entity">Toren Capital Pty. Ltd</div>
    </header>
    <div class="strip"></div>
    <div class="content">
      <div class="main">
        <h1>Risk Management</h1>
        <div class="photo-row" style="height:116px">
          <div class="photo" role="img" aria-label="Hand drawing on a financial line graph" style="background:linear-gradient(135deg,#f4f4f4,#9ea3aa 50%,#3c3f45)"></div>
          <div class="photo" role="img" aria-label="Green dice on a dark table" style="background:linear-gradient(135deg,#e9ecdf,#8d9a5e 50%,#2f3422)"></div>
          <div class="photo" role="img" aria-label="Presenter showing a chart to colleagues in a meeting" style="background:linear-gradient(135deg,#eef3f8,#a3b3c6 50%,#50607a)"></div>
        </div>
        <p>Lorem ipsum dolor sit amet, consectetur adipiscing elit. Nam pulvinar ultrices magna, nec blandit quam luctus id. Vivamus sagittis iaculis convallis. Phasellus vestibulum, ipsum nec vestibulum venenatis, erat lorem consequat tellus, tincidunt consequat neque ipsum id metus. Morbi at lorem purus.</p>
        <div class="risk-grid">
          <div class="chart-title" style="left:16px;top:4px">Gross Exposure</div>
          <svg style="left:0;top:20px" width="110" height="170" viewBox="0 0 110 170" font-size="5" fill="#555">
            <g text-anchor="end"><text x="14" y="8">160</text><text x="14" y="27">140</text><text x="14" y="46">120</text><text x="14" y="65">100</text><text x="14" y="84">80</text><text x="14" y="103">60</text><text x="14" y="122">40</text><text x="14" y="141">20</text><text x="14" y="160">0</text></g>
            <line x1="20" y1="4" x2="20" y2="158" stroke="#444"/><line x1="20" y1="158" x2="100" y2="158" stroke="#444"/>
            <rect x="36" y="50" width="46" height="30" fill="#5fb9e6"/><rect x="36" y="80" width="46" height="78" fill="var(--blue-dark)"/>
            <text x="59" y="67" text-anchor="middle" fill="#fff" font-size="4.5">potential</text><text x="59" y="112" text-anchor="middle" fill="#fff" font-size="4.5">actual</text>
          </svg>
          <div class="chart-title" style="left:22px;top:222px">Net Exposure</div>
          <svg style="left:0;top:240px" width="110" height="170" viewBox="0 0 110 170" font-size="5" fill="#555">
            <g text-anchor="end"><text x="14" y="8">160</text><text x="14" y="27">140</text><text x="14" y="46">120</text><text x="14" y="65">100</text><text x="14" y="84">80</text><text x="14" y="103">60</text><text x="14" y="122">40</text><text x="14" y="141">20</text><text x="14" y="160">0</text></g>
            <line x1="20" y1="4" x2="20" y2="158" stroke="#444"/><line x1="20" y1="158" x2="100" y2="158" stroke="#444"/>
            <rect x="36" y="30" width="46" height="30" fill="#5fb9e6"/><rect x="36" y="60" width="46" height="98" fill="var(--blue-dark)"/>
            <text x="59" y="47" text-anchor="middle" fill="#fff" font-size="4.5">potential</text><text x="59" y="100" text-anchor="middle" fill="#fff" font-size="4.5">actual</text>
          </svg>
          <div class="vrule" style="left:150px;top:0;height:430px"></div>
          <div class="chart-title" style="left:190px;top:4px">Strategy Allocation</div>
          <svg style="left:178px;top:20px" width="140" height="80" viewBox="0 0 140 80" font-size="4.5" fill="#555">
            <g transform="translate(76 40) rotate(-90)"><circle r="14" fill="none" stroke="#1a6fb8" stroke-width="28" pathLength="100" stroke-dasharray="70 30"/><circle r="14" fill="none" stroke="#9fd4ee" stroke-width="28" pathLength="100" stroke-dasharray="10 90" stroke-dashoffset="-70"/><circle r="14" fill="none" stroke="#cfe7e2" stroke-width="28" pathLength="100" stroke-dasharray="20 80" stroke-dashoffset="-80"/></g>
            <text x="116" y="12">ARB</text><text x="116" y="18">20%</text><text x="116" y="34">IPO</text><text x="116" y="40">10%</text><text x="12" y="48">Special Sits</text><text x="20" y="54">70%</text>
          </svg>
          <div class="chart-title" style="left:190px;top:150px">Country Allocation</div>
          <svg style="left:178px;top:166px" width="140" height="80" viewBox="0 0 140 80" font-size="4.5" fill="#555">
            <g transform="translate(76 40) rotate(-90)"><circle r="14" fill="none" stroke="#1a6fb8" stroke-width="28" pathLength="100" stroke-dasharray="70 30"/><circle r="14" fill="none" stroke="#9fd4ee" stroke-width="28" pathLength="100" stroke-dasharray="10 90" stroke-dashoffset="-70"/><circle r="14" fill="none" stroke="#cfe7e2" stroke-width="28" pathLength="100" stroke-dasharray="20 80" stroke-dashoffset="-80"/></g>
            <text x="116" y="12">ARB</text><text x="116" y="18">20%</text><text x="116" y="34">IPO</text><text x="116" y="40">10%</text><text x="12" y="48">Special Sits</text><text x="20" y="54">70%</text>
          </svg>
          <div class="chart-title" style="left:194px;top:296px">Sector Allocation</div>
          <svg style="left:178px;top:312px" width="140" height="80" viewBox="0 0 140 80" font-size="4.5" fill="#555">
            <g transform="translate(76 40) rotate(-90)"><circle r="14" fill="none" stroke="#1a6fb8" stroke-width="28" pathLength="100" stroke-dasharray="70 30"/><circle r="14" fill="none" stroke="#9fd4ee" stroke-width="28" pathLength="100" stroke-dasharray="10 90" stroke-dashoffset="-70"/><circle r="14" fill="none" stroke="#cfe7e2" stroke-width="28" pathLength="100" stroke-dasharray="20 80" stroke-dashoffset="-80"/></g>
            <text x="116" y="12">ARB</text><text x="116" y="18">20%</text><text x="116" y="34">IPO</text><text x="116" y="40">10%</text><text x="12" y="48">Special Sits</text><text x="20" y="54">70%</text>
          </svg>
          <div class="vrule" style="left:345px;top:0;height:430px"></div>
          <table style="left:362px;top:0">
            <caption>Historical Risk Parameters</caption>
            <tr><td>Standard Deviation</td><td>6.4</td></tr><tr><td>Sortino</td><td>1.92</td></tr><tr><td>Sharpe</td><td>1.58</td></tr>
          </table>
          <table style="left:362px;top:70px">
            <caption>Live Portfolio Risk</caption>
            <tr><th>Parameters</th><th>Max</th><th>Current</th></tr>
            <tr><td>Single Name</td><td>5</td><td>3</td></tr><tr><td>Sector</td><td>30</td><td>18</td></tr><tr><td>Country</td><td>50</td><td>32</td></tr><tr><td>Gross</td><td>150</td><td>96</td></tr><tr><td>Net</td><td>+/- 50</td><td>12</td></tr><tr><td>VaR</td><td>3</td><td>1.4</td></tr>
          </table>
          <table style="left:362px;top:176px">
            <caption>Estimated MTD Return</caption>
            <tr><th>Strategy Contribution</th><th>%</th></tr>
            <tr><td>IPO</td><td>0.6</td></tr><tr><td>ARB</td><td>0.35</td></tr><tr><td>SLSSTS</td><td>1.2</td></tr><tr><td>TOTAL</td><td>2.15</td></tr>
          </table>
          <table style="left:362px;top:262px">
            <caption>Live Portfolio Risk</caption>
            <tr><th>Top 5 Positions</th><th>Long / Short</th><th>% NAV</th></tr>
            <tr><td>Mining Co</td><td>Long</td><td>5%</td></tr><tr><td>Telecom Co</td><td>Long</td><td>4%</td></tr><tr><td>Harbor Resources</td><td>Short</td><td>4%</td></tr><tr><td>Bank</td><td>Short</td><td>3%</td></tr><tr><td>Brewery</td><td>Long</td><td>3%</td></tr>
          </table>
        </div>
      </div>
      <aside class="sidebar"><a>Our Focus</a><a>Contact Us</a><div class="gap"></div><a>Quick Links</a><a>Toren Home</a><a>Contact Us</a></aside>
    </div>
    <footer class="site-footer"><div class="footer-accent"></div><div class="footer-links"><a>Privacy Policy</a><a>Disclaimer</a></div></footer>
  </div>
  <div class="credit" style="top:828px">Toren Capital Pty Ltd</div>
</section>

</body>
</html>
```